Landing page and nested content pages for HearthlightFaith.com

Web design for existing site https://hearthlightfaith.example/

This is a RESPONSIVE web site that needs to work on a medium-res mobile device and also look great on a widescreen desktop.

There are three or four public pages we currently have that need a fresh design, which will be used somewhat to guide the design direction for the non-public interior site for logged-in users in a later design effort.

The recently created new logo is attached and the new design should be based on this logo, I don't know how you'll do it, but the new logo should fit appropriately; the current web site's little logo on the top left must be thrown out, and one of our goals in this design effort is to set up the top nav bar, logo placement, etc. There are multiple logos attached to this project but the primary one to try for is the red door one. The other logos (gray+red arc logo and tree logo) are there in case you as the designer prefer them and can demonstrate that they are more suited for a web design than the red one. Otherwise I am hoping to see the red logo used for the site overall and the other logos to highlight discipleship and/or fellowship sections on the site.

The main pages are: 1) landing page, which describes the function of the site for logged-in users (not actually a part of this design project but the logged-in users' site redesign should be inspired by this effort) with multiple bits of content embedded on the page, and 2) a content page called "The Cornerstones" which contains several pages worth of content. The content is currently just a wall of text; it needs to be somehow broken down into clickable sections and imagery applied to make it interesting. 3) We also have some more minor pages which I'll list below.

The Landing Page

This is to redesign the content at https://hearthlightfaith.example/
The current web site's placeholder content represents the general direction desired for the landing page, but I'm not a designer, so colors and layout etc can be totally re-thought. I'd like to use these images and these highlights. I've uploaded the stock images.

The web site on the whole for logged-in users (again, not itself a part of this design) is part social network and part library of various guides and resources. So the landing page needs to highlight the objectives of the site while demonstrating some of the features of the site. There is currently also some additional text content that should also be there, but should not be so prominently displayed as it is today; it should be accessible from some scrolling and/or from a button-click pop-over, so that new visitors are not inundated with a wall of text. Besides the logo, I've uploaded some features of the site that might be useful in graphically highlighting the features of the site.

'The Cornerstones' Content Page

This is to redesign the content at https://hearthlightfaith.example/Gospel

The content at this URL is currently one big wall of text, and it is intimidating enough that people may not be likely to read it. It needs to be read.

Other minor content pages

We also have these pages that needs to demonstrate a "theme" of basic content pages' design strategy for basic content:

https://hearthlightfaith.example/freebibleresponse
and
https://hearthlightfaith.example/bibledistribution

We will be adding additional content pages later, but we need to finalize the design theme before proceeding.

As currently demonstrated, I tend to prefer a serif font for headings (for theming around ancient-yet-current faith-based content), sans-serif for paragraphs (for readability), which is why the current site uses the fonts it has. Find some better fonts as you please.

The images prefixed with "interior-features-" are for landing page reference only, you might choose to highlight a cropped snippet, but don't go too crazy since these features will themselves be redesigned and so we will need to replace whatever cropped sample you might use with another one later.

There will be login and register functions. I DO NOT want any of this functionality to be built, but I do want the core public-site UX concept built out with *CLEAN* and attractive markup in HTML+CSS(+JS?) based on Bootstrap 4.

Target Market(s)

Christians looking for fellowship and discipleship outside of traditional church buildings (in-home fellowship, online fellowship, online study resources)

Requirements
Must have
• Landing page entices the user to register
'Cornerstones' page somehow redistributes content into meaningful sections
Other minor content pages are redesigned but not too complicated, so that future content pages can follow suit
Designer can choose the logo out of 3, but the red door logo was the preferred logo if you can work with it and integrate it into the site such as with a responsive site top nav bar logo
HTML+CSS must be clean and based on Bootstrap 4

```html
<!DOCTYPE html>
<html lang="en">
<head>
<meta charset="utf-8">
<title>Hearthlight Faith</title>
<link rel="stylesheet" href="https://fonts.googleapis.com/css2?family=Montserrat:wght@500;600&family=Raleway:wght@400;500&display=swap">
<style>
:root{
  --red:#b81c2e;
  --red-dark:#9e1626;
  --ink:#333333;
  --muted:#6b6b6b;
  --light:#f4f4f4;
  --white:#ffffff;
  --footer:#353535;
}
*{box-sizing:border-box;margin:0;padding:0}
html,body{width:1200px;height:3419px;overflow:hidden}
body{font-family:"Raleway",sans-serif;color:var(--ink);background:var(--white)}
.page{position:relative;width:1200px;height:3419px}
h1,h2,h3{font-family:"Montserrat",sans-serif;font-weight:500;text-transform:uppercase}
.btn{position:absolute;display:flex;align-items:center;justify-content:center;white-space:nowrap;background:var(--red);color:var(--white);font-family:"Montserrat",sans-serif;font-weight:500;font-size:17px;border-radius:26px;text-transform:uppercase;text-decoration:none;box-shadow:0 2px 4px rgba(0,0,0,.15)}
.nowrap{white-space:nowrap}

/* header */
.site-header{position:absolute;left:0;top:0;width:1200px;height:134px;background:var(--white)}
.brand{position:absolute;left:113px;top:44px;display:flex;align-items:center;gap:10px;font-family:"Montserrat",sans-serif;font-weight:600;font-size:19px;color:var(--red);letter-spacing:.5px}
.brand-mark{width:26px;height:26px;background:var(--red)}

/* hero */
.hero{position:absolute;left:0;top:134px;width:1200px;height:686px;background:linear-gradient(100deg,#c99a7a 0%,#a37a5a 22%,#6b6a34 45%,#8a6a3c 62%,#b79a86 80%,#9c8f86 100%)}
.hero-glow{position:absolute;inset:0;background:radial-gradient(circle at 38% 28%,rgba(255,220,170,.55),transparent 45%),linear-gradient(180deg,transparent 50%,rgba(60,70,20,.45))}
.hero-title{position:absolute;left:106px;top:410px;font-size:49px;color:var(--white);letter-spacing:.5px}
.hero-text{position:absolute;left:112px;top:483px;width:500px;font-size:16.5px;line-height:33px;color:var(--white)}
.hero-arrow{position:absolute;top:460px}

/* welcome */
.welcome-title{position:absolute;left:0;top:920px;width:1200px;text-align:center;font-size:32px;color:var(--red)}
.welcome-lead{position:absolute;left:360px;top:970px;width:480px;text-align:center;font-size:15px;line-height:27px;color:#222}
.rule{position:absolute;left:567px;top:1045px;width:66px;height:1px;background:#777}
.welcome-body{position:absolute;left:188px;top:1070px;width:824px;text-align:center;font-size:14px;line-height:30.5px;color:var(--muted)}

/* features */
.features{position:absolute;left:0;top:1371px;width:1200px;height:959px}
.tile{position:absolute;width:592px;height:471px}
.tile-nw{left:0;top:0;background:linear-gradient(135deg,#6b5a4a,#9a8a72 45%,#b8ab96 70%,#5d4a36)}
.tile-ne{left:608px;top:0;background:linear-gradient(110deg,#7a6a5a,#6a6048 40%,#9a8a80 70%,#8c8a88)}
.tile-sw{left:0;top:488px;background:linear-gradient(135deg,#3a2e26,#6a5a4a 40%,#b8aa98 65%,#4a3a30)}
.tile-se{left:608px;top:488px;background:linear-gradient(120deg,#6f7d88,#3e5366 40%,#2a4c8a 70%,#3a3a40)}
.tile::after{content:"";position:absolute;inset:0;background:rgba(0,0,0,.28)}
.tile-text{position:absolute;left:20px;z-index:2;color:var(--white)}
.tile-text h3{font-size:21px;margin-bottom:12px;letter-spacing:.3px;white-space:nowrap}
.tile-text p{font-size:13.5px;line-height:28px;width:425px}
.tile-top .tile-text{top:46px}
.tile-bottom .tile-text{top:342px}
.diamond{position:absolute;left:373px;top:253px;width:454px;height:454px;transform:rotate(45deg);border:4px solid var(--white);background:linear-gradient(135deg,rgba(200,40,60,.88),rgba(184,28,46,.9));z-index:3}
.diamond-text{position:absolute;left:330px;top:410px;width:540px;text-align:center;color:var(--white);z-index:4}
.diamond-text h3{font-size:21px;line-height:33px;letter-spacing:.3px}
.diamond-text p{margin:22px auto 0;width:510px;font-size:14.5px;line-height:33px}

/* coming */
.coming{position:absolute;left:0;top:2330px;width:1200px;height:364px;background:var(--light)}
.coming h2{position:absolute;left:0;top:92px;width:1200px;text-align:center;font-size:36px;color:var(--red)}
.coming p{position:absolute;left:250px;top:148px;width:700px;text-align:center;font-size:15.5px;line-height:33px;color:#222}

/* meantime */
.meantime-title{position:absolute;left:111px;top:2822px;width:440px;font-size:33px;line-height:41.5px;color:var(--red)}
.meantime-body{position:absolute;left:111px;top:3003px;width:440px;font-size:15.5px;line-height:31px;color:#444}
.meantime-photo{position:absolute;left:575px;top:2797px;width:513px;height:445px;background:linear-gradient(150deg,#7a848c,#b8a890 35%,#d9c7a8 60%,#8a6a80 85%,#5a5f6a);box-shadow:0 2px 6px rgba(0,0,0,.2)}

/* footer */
.site-footer{position:absolute;left:0;top:3344px;width:1200px;height:75px;background:var(--footer);color:var(--white);text-align:center;font-family:"Montserrat",sans-serif;font-size:15.5px;line-height:75px;letter-spacing:.3px}
</style>
</head>
<body>
<div class="page">

  <header class="site-header">
    <div class="brand"><span class="brand-mark"></span>HEARTHLIGHT FAITH</div>
    <a class="btn" href="#" style="left:763px;top:53px;width:154px;height:50px">Register</a>
    <a class="btn" href="#" style="left:934px;top:53px;width:154px;height:50px">Log In</a>
  </header>

  <section class="hero" role="img" aria-label="Young woman with closed eyes holding a Bible to her chest in a sunlit field">
    <div class="hero-glow"></div>
  </section>
  <svg class="hero-arrow" style="left:64px" width="22" height="32" viewBox="0 0 22 32"><path d="M17 3 L5 16 L17 29" fill="none" stroke="#fff" stroke-width="3"/></svg>
  <svg class="hero-arrow" style="left:1112px" width="22" height="32" viewBox="0 0 22 32"><path d="M5 3 L17 16 L5 29" fill="none" stroke="#fff" stroke-width="3"/></svg>
  <h1 class="hero-title">Hearthlight Faith</h1>
  <p class="hero-text">Form fellowships, bible studies, home churches, and participate in activities with church establishments.</p>
  <a class="btn" href="#" style="left:111px;top:559px;width:153px;height:50px;font-size:16px">Get Started</a>

  <h2 class="welcome-title">Welcome, Neighbor!</h2>
  <p class="welcome-lead">Lorem ipsum dolor sit amet, consectetur adipiscing elit, sed do eiusmod tempor incididunt ut</p>
  <div class="rule"></div>
  <p class="welcome-body">This web site is still in its early pre-planning stages and what you currently see here are some somewhat functional resources pertaining to the larger objectives. Those objectives are primarily to encourage local believers in any neighborhood around the world to read the Bible, (re-?)discover God and His presence, become disciples, and make disciples, independently of or in complement to the auspices of the institutional church</p>
  <a class="btn" href="#" style="left:523px;top:1216px;width:154px;height:51px">Read More</a>

  <section class="features">
    <div class="tile tile-nw tile-top" role="img" aria-label="Two neighbors greeting each other over a wooden fence">
      <div class="tile-text"><h3>Find Nearby Believers</h3><p>Form fellowships, bible studies, home churches, and participate in activities with church establishments.</p></div>
    </div>
    <div class="tile tile-ne tile-top" role="img" aria-label="Young woman holding a Bible at sunset">
      <div class="tile-text" style="left:27px"><h3>Share Your Heart and Mind</h3><p style="width:345px">Post your thoughts or publish articles pertaining to the faith, receive feedback from other believers.</p></div>
    </div>
    <div class="tile tile-sw tile-bottom" role="img" aria-label="Group holding hands in prayer over open Bibles on a table">
      <div class="tile-text"><h3>Meet, Grow, and Pray Together.</h3><p style="width:470px">Meet together, online or in person. Praise and worship Jesus together. Teach one another. Admonish and exhort. Pray for one another in love.</p></div>
    </div>
    <div class="tile tile-se tile-bottom" role="img" aria-label="People seated in a circle holding hands in prayer">
      <div class="tile-text" style="left:30px"><h3>Schedule Outreaches</h3><p style="width:395px">Commit to reaching out to the community, bringing food, clothing, or just lots of God's love.</p></div>
    </div>
    <div class="diamond" role="img" aria-label="Crowd of children at a mission outreach, tinted red"></div>
    <div class="diamond-text">
      <h3>Go Global, to Every Tribe,<br>Every Tongue, Every Nation.</h3>
      <p>Find and support organizations that are reaching around the world to share the love of Jesus, or go yourself.</p>
    </div>
  </section>

  <section class="coming">
    <h2>It's Coming</h2>
    <p>We just got this place, come back in a bit. If you want to reach out, send an<br><span class="nowrap">e-mail</span> to ada@hearthlightfaith.example</p>
    <a class="btn" href="#" style="left:438px;top:239px;width:153px;height:51px">Register</a>
    <a class="btn" href="#" style="left:609px;top:239px;width:153px;height:51px">Log In</a>
  </section>

  <h2 class="meantime-title">In the Mean Time,<br>Read the<br>"Cornerstones"<br>Content</h2>
  <p class="meantime-body">View summary of how and why to read the Bible, and of the Gospel presented in the Bible. Please email us if you want to reach out, for any reason.</p>
  <a class="btn" href="#" style="left:111px;top:3119px;width:236px;height:51px">View Cornerstones</a>
  <div class="meantime-photo" role="img" aria-label="Young people around a table studying open Bibles together"></div>

  <footer class="site-footer">© 2021 ALL RIGHTS RESERVED</footer>
</div>
</body>
</html>
```